Create a bold and border around my logo to make it pop and sign graphic design

I would like someone to create a sign graphic design so I can use on the side of my trucks and put on yard signs. I would to remove a lot of the white and add more of the orange and blue to give it more pop when cars drive past. I would like the services to be removed and for you to leave space for a mobile number that i would add later. I don’t want my logo changed at all. I just want colour and design to be added to the background so i can use it in signage. Same colour as on the sign

```html
<!DOCTYPE html>
<html lang="en">
<head>
<meta charset="utf-8">
<title>Branchworthy – Vehicle &amp; Yard Sign</title>
<link rel="stylesheet" href="https://fonts.googleapis.com/css2?family=Montserrat:wght@600&display=swap">
<style>
  :root {
    --brand-orange: #e04510;
    --brand-orange-deep: #d63a08;
    --brand-navy: #0b2c6c;
    --brand-navy-deep: #08255e;
    --sign-white: #ffffff;
    --stage: #1c0703;
  }
  * { margin: 0; padding: 0; box-sizing: border-box; }
  html, body {
    width: 1200px;
    height: 709px;
    overflow: hidden;
    background: var(--stage);
  }
  .sign {
    position: absolute;
    left: 40px;
    top: 68px;
    width: 1120px;
    height: 572px;
    overflow: hidden;
    background: var(--sign-white);
    font-family: "Montserrat", sans-serif;
    font-weight: 600;
  }
  .sign__top-band {
    position: absolute;
    left: 0; top: 0;
    width: 100%;
    height: 280px;
    background: linear-gradient(115deg, var(--brand-orange) 0%, var(--brand-orange-deep) 45%, var(--brand-orange) 100%);
  }
  .sign__emblem {
    position: absolute;
    left: 383px;
    top: 4px;
    width: 346px;
    height: 346px;
    border-radius: 50%;
    background: var(--sign-white);
  }
  .sign__name-band {
    position: absolute;
    left: 0; top: 280px;
    width: 100%;
    height: 137px;
    background: var(--sign-white);
    display: flex;
    align-items: center;
    justify-content: center;
  }
  .sign__name {
    font-size: 88px;
    line-height: 1;
    letter-spacing: 2px;
    color: var(--brand-navy);
    padding-top: 6px;
  }
  .sign__contact-band {
    position: absolute;
    left: 0; top: 417px;
    width: 100%;
    height: 155px;
    background: linear-gradient(115deg, var(--brand-navy-deep) 0%, var(--brand-navy) 50%, var(--brand-navy-deep) 100%);
    display: flex;
    align-items: center;
    justify-content: center;
    gap: 18px;
  }
  .sign__phone-icon {
    width: 70px;
    height: 88px;
    fill: var(--sign-white);
  }
  .sign__phone-number {
    font-size: 104px;
    line-height: 1;
    color: var(--sign-white);
    letter-spacing: 1px;
  }
</style>
</head>
<body>
  <main class="sign">
    <div class="sign__top-band"></div>
    <div class="sign__emblem"></div>
    <div class="sign__name-band">
      <h1 class="sign__name">BRANCHWORTHY</h1>
    </div>
    <div class="sign__contact-band">
      <svg class="sign__phone-icon" viewBox="0 0 24 30" aria-hidden="true">
        <path d="M5.2 1.2 8.6 0.4c.7-.2 1.4.2 1.6.9l1.6 5.6c.2.6-.1 1.3-.7 1.6L8.4 9.8c1 4.6 3.4 8.7 6.8 11.8l2.5-1.6c.6-.4 1.3-.3 1.8.2l3.8 4.4c.5.5.4 1.3-.1 1.8l-2.6 2.4c-1 .9-2.5 1.1-3.7.5C7.6 25.2 2.2 16.6 2.6 5.4c.1-2 1-3.7 2.6-4.2z"/>
      </svg>
      <p class="sign__phone-number">0198765432</p>
    </div>
  </main>
</body>
</html>
```